Plumvale CEO needs a Crowdsourced Graphic for a Wirelark Article

I need a simple graphic / banner for a blog post that's going to be posted on Wirelark (www.wirelark.com) - the biggest tech blog in the world.

The article will be written by Tobin Marsh (Plumvale's CEO) and the title will be "Asia's Secret Crowdsourcing Boom". The article is about the tens of thousands of people using crowdsourcing websites (like Plumvale.com, Qorvel.com and Vantrio.com) in China, India, the Philippines, Australia and other countries in the Asia Pacific region.

We'd really like to get this ASAP - so early submissions encouraged. We will try and get the winning designer linked to from the article.

Thanks to everyone that submitted!  Some great designs and hard to choose! :)

Target Market(s)

Tech saavy readers, English speakers

Industry/Entity Type

Tech

Requirements
Must have
• The graphic SHOULD:
1) Have the text "Asia's secret crowdsourcing boom" with some nice design and fonts (consider grey subtle pattern background and white drop shadow on fonts) - see attached examples
2) Have an Asian theme
3) Have the dimensions 640px wide by 240px wide
Nice to have
• The graphic COULD:
1) Have references to some or all of the countries mentioned above or use Asian characters as part of the background / motif (maybe the word "crowd" or "crowd sourcing" in different languages). In Chinese, the word for crowdsourcing is "witkey" (and there are corresponding Chinese characters: ??)
2) Emphasize the word "Asia" (using color and larger/different font)
3) Use a chart showing exponential (i.e. fast) growth - like the attached
4) Have a second line of text "5 Things You Didn't Know About Crowdsourcing in Asia"

```html
<!DOCTYPE html>
<html lang="en">
<head>
<meta charset="utf-8">
<title>Asia's Secret Crowdsourcing Boom</title>
<link rel="stylesheet" href="https://fonts.googleapis.com/css2?family=Anton&family=Oswald:wght@600;700&family=Noto+Sans+SC:wght@700&family=Noto+Sans+KR:wght@700&family=Noto+Sans+Thai:wght@700&display=swap">
<style>
  :root {
    --paper: #efefef;
    --stripe: #e6e6e6;
    --ghost: #d6d6d6;
    --ghost-dark: #cdcdcd;
    --asia-red: #c8242b;
    --headline-blue: #1a6fc0;
    --chart-red: #c8242b;
    --dot-fill: #ffffff;
  }
  html, body {
    margin: 0;
    padding: 0;
    overflow: hidden;
    background: #ffffff;
  }
  .banner {
    position: relative;
    width: 1200px;
    height: 450px;
    overflow: hidden;
    background-color: var(--paper);
    background-image: repeating-linear-gradient(135deg, var(--stripe) 0 2px, transparent 2px 7px);
  }
  .banner svg {
    position: absolute;
    inset: 0;
    display: block;
  }
  .ghost-word { fill: var(--ghost); }
  .ghost-hanzi { font-family: "Noto Sans SC", sans-serif; font-weight: 700; }
  .ghost-hangul { font-family: "Noto Sans KR", sans-serif; font-weight: 700; fill: var(--ghost); opacity: .8; }
  .ghost-thai { font-family: "Noto Sans Thai", sans-serif; font-weight: 700; font-style: italic; fill: var(--ghost-dark); }
  .ghost-latin { font-family: "Oswald", sans-serif; font-weight: 600; }
  .ghost-witkey { font-family: "Oswald", sans-serif; font-weight: 700; fill: var(--ghost-dark); }
  .growth-line { fill: none; stroke: var(--chart-red); stroke-width: 7; stroke-linejoin: round; stroke-linecap: round; }
  .growth-dot { fill: var(--dot-fill); stroke: var(--chart-red); stroke-width: 6; }
  .title-asia { font-family: "Anton", sans-serif; fill: var(--asia-red); }
  .title-line { font-family: "Oswald", sans-serif; font-weight: 700; fill: var(--headline-blue); }
  .title-boom { font-family: "Anton", sans-serif; fill: var(--headline-blue); }
  .shadow { filter: drop-shadow(2px 2px 0 #ffffff); }
</style>
</head>
<body>
<div class="banner">
  <svg width="1200" height="450" viewBox="0 0 1200 450" aria-labelledby="banner-title">
    <title id="banner-title">Asia's Secret Crowdsourcing Boom</title>

    <g class="background-words" aria-hidden="true">
      <text class="ghost-word ghost-hanzi" x="600" y="80" font-size="110">集団</text>
      <text class="ghost-hangul" x="440" y="215" font-size="90">군중</text>
      <text class="ghost-thai" x="45" y="395" font-size="92" textLength="560" lengthAdjust="spacingAndGlyphs">ฝูงชนภูมิภาคเอเชีย</text>
      <text class="ghost-word ghost-latin" x="940" y="245" font-size="100">grupo</text>
      <text class="ghost-witkey" x="985" y="433" font-size="58">witkey</text>
    </g>

    <g class="growth-chart" aria-hidden="true">
      <polyline class="growth-line" points="497,460 585,396 707,384 780,334 874,341 1072,86"/>
      <circle class="growth-dot" cx="585" cy="396" r="13"/>
      <circle class="growth-dot" cx="707" cy="384" r="13"/>
      <circle class="growth-dot" cx="780" cy="334" r="13"/>
      <circle class="growth-dot" cx="874" cy="341" r="13"/>
      <circle class="growth-dot" cx="1072" cy="86" r="13"/>
    </g>

    <g class="headline shadow">
      <text class="title-asia" x="46" y="188" font-size="170" textLength="452" lengthAdjust="spacingAndGlyphs">ASIA's</text>
      <text class="title-line" x="52" y="262" font-size="64" textLength="692" lengthAdjust="spacingAndGlyphs">SECRET CROWDSOURCING</text>
      <text class="title-boom" font-size="100">
        <tspan x="762" y="262" rotate="-4">B</tspan>
        <tspan x="818" y="270" rotate="3">O</tspan>
        <tspan x="872" y="250" rotate="-6">O</tspan>
        <tspan x="926" y="264" rotate="5">M</tspan>
      </text>
    </g>
  </svg>
</div>
</body>
</html>
```